Corvane PowerPoint Template for Board of Directors Meeting and General Use

Need a clean fresh PowerPoint slide deck with lots of white space. Fun and creative, if possible. Colors can be referred to from our website (okappahub.example), and brand style guide is attached. Website is blah. Please give the deck a little more energy if possible. (colors: teals/purples/grays).
Corvane logo needs to be placed consistently throughout the deck.
Can incorporate but not required TREL and FLUKE (logos only) and additional design as clip art.
Also, to incorporate on one or two slides is the Corvane Encompassing Logo. This is a mockup logo and we were hoping you could play around with it and change some things for us. If you are able to change the background colors on this mock logo to more properly match our Corvane colors (teal, purple, grey) that would be amazing. Also, try adding the Corvane logo under the globe image in the center. Finally, if we can have the more cartoon icons on the left side replaced with similar images that more closely reflect the designs on the right hand side, that would be perfect.
This is for a board of directors meeting, but also for general internal use.
Several page options of slide deck needed. (title, content, content + photo/chart, etc)
Target Market(s)
Interal Staff and Board of Directors
Industry/Entity Type
Trade Association for Data Destruction, Data Privacy, Records Storage
Look and feel

```html
<!DOCTYPE html>
<html lang="en">
<head>
<meta charset="utf-8">
<title>Corvane Slide Deck Template</title>
<link href="https://fonts.googleapis.com/css2?family=Catamaran:wght@500;700&family=Questrial&family=Oswald:wght@400&display=swap" rel="stylesheet">
<style>
:root{
  --stage:#8a9e9f;
  --teal:#005a5b;
  --white:#ffffff;
  --ink:#2c3a3b;
  --gray:#a9b0b2;
  --gray-light:#c9cdce;
  --purple:#7c6d8e;
  --photo-mid:#6f8587;
  --foot-on-teal:#9fb8b8;
}
*{box-sizing:border-box;margin:0;padding:0}
html,body{width:1200px;height:573px;overflow:hidden;background:var(--stage)}
body{position:relative;font-family:"Questrial",sans-serif;color:var(--ink)}
.slide{position:absolute;width:267px;height:150px;background:var(--white);overflow:hidden}
.slide *{position:absolute}
.slide svg *{position:static}
.c{transform:translateX(-50%);text-align:center}
.title{font-family:"Catamaran",sans-serif;font-weight:700;color:var(--white);white-space:nowrap}
.header{left:0;top:0;width:267px;height:29px;background:linear-gradient(90deg,var(--teal) 0%,var(--teal) 62%,var(--photo-mid) 82%,var(--purple) 100%)}
.header .title{left:20px;top:8px;font-size:10px;line-height:12px}
.foot{right:8px;bottom:5px;display:flex;align-items:center;gap:3px}
.foot *{position:static}
.foot .word{font-family:"Catamaran",sans-serif;font-weight:700;font-size:7.5px;line-height:9px;color:var(--gray)}
.foot .dot{width:6px;height:6px;border-radius:50%;background:var(--gray)}
.on-teal .foot .word{color:var(--foot-on-teal)}
.on-teal .foot .dot{background:var(--foot-on-teal)}
.body{font-size:4.3px;line-height:5.6px;color:var(--ink)}
.tiny{font-size:2.4px;line-height:3px;color:var(--gray)}
.tiny-dark{font-size:2.4px;line-height:3px;color:var(--teal);font-family:"Catamaran",sans-serif}
.label{font-family:"Catamaran",sans-serif;font-weight:700;font-size:5px;line-height:6px;color:var(--teal);white-space:nowrap}
.bullet{white-space:nowrap;color:var(--ink)}
.bullet::before{content:"";position:absolute;left:-1.5em;top:.3em;width:.7em;height:.7em;border:.14em solid var(--teal);border-radius:50%}
.signoff{left:0;top:107px;width:267px;height:43px;display:flex;align-items:center;justify-content:center;gap:6px}
.signoff *{position:static}
.signoff .word{font-family:"Catamaran",sans-serif;font-weight:700;font-size:18px;line-height:20px;color:var(--teal)}
.signoff .dot{width:14px;height:14px;border-radius:50%;background:var(--teal)}
</style>
</head>
<body>

<svg width="0" height="0" style="position:absolute" aria-hidden="true">
  <defs>
    <symbol id="i-heart" viewBox="0 0 24 24"><path d="M12 20.5 4.2 12.8A4.8 4.8 0 0 1 12 6.5a4.8 4.8 0 0 1 7.8 6.3Z" fill="none" stroke="currentColor" stroke-width="1.2" stroke-linejoin="round"/></symbol>
    <symbol id="i-folder" viewBox="0 0 24 24"><path d="M3 7h6l2 2h8v9H3Z M3 18l3-7h16l-3 7" fill="none" stroke="currentColor" stroke-width="1.1" stroke-linejoin="round"/></symbol>
    <symbol id="i-bulb" viewBox="0 0 24 24"><path d="M9 15.5c0-2-3-3.3-3-7a6 6 0 0 1 12 0c0 3.7-3 5-3 7Z M9.5 17.5h5 M10 19.5h4" fill="none" stroke="currentColor" stroke-width="1.1" stroke-linecap="round"/></symbol>
    <symbol id="i-gear" viewBox="0 0 24 24"><path d="M12 3.5l1.6.3.5 2.2 1.6.9 2.1-.8 1.2 1.2-.8 2.1.9 1.6 2.2.5v2l-2.2.5-.9 1.6.8 2.1-1.2 1.2-2.1-.8-1.6.9-.5 2.2h-2l-.5-2.2-1.6-.9-2.1.8-1.2-1.2.8-2.1-.9-1.6-2.2-.5v-2l2.2-.5.9-1.6-.8-2.1 1.2-1.2 2.1.8 1.6-.9.5-2.2Z" fill="none" stroke="currentColor" stroke-width="1" stroke-linejoin="round"/><circle cx="12" cy="12" r="3" fill="none" stroke="currentColor" stroke-width="1"/></symbol>
  </defs>
</svg>

<!-- Row 1 -->
<section class="slide on-teal" style="left:46.6px;top:45.2px;background:var(--teal)">
  <div role="img" aria-label="Title photograph: circuit boards and shredded documents in gray, teal and purple tones" style="left:0;top:0;width:267px;height:110px;background:linear-gradient(120deg,#9aa6a6 0%,#c7c6c8 30%,#b2b2b6 55%,#8f8f9b 78%,#7d6a8b 100%)"></div>
  <div style="left:0;top:60px;width:120px;height:50px;background:linear-gradient(20deg,rgba(0,90,91,.7),rgba(0,90,91,0) 70%)"></div>
  <div class="title" style="left:13px;top:119px;font-size:16px;line-height:18px">Corvane</div>
  <div class="title" style="left:114.6px;top:117px;font-size:11px;line-height:13px">Click to edit Master title style</div>
  <div style="left:114.6px;top:131px;font-size:5.5px;line-height:6px;color:var(--white)">Click to edit Master subtitle style</div>
</section>

<section class="slide on-teal" style="left:321.4px;top:45.2px">
  <div style="left:0;top:92.7px;width:267px;height:58px;background:var(--teal)"></div>
  <div class="title" style="left:19.6px;top:102px;font-size:11px;line-height:13px">Click to edit Master title style</div>
  <div style="left:19.6px;top:117px;font-size:5.5px;line-height:6px;color:var(--white)">Click to edit Master subtitle style</div>
</section>

<section class="slide" style="left:597.2px;top:45.2px">
  <div class="header"><div class="title">Click to edit Master title style</div></div>
  <div class="bullet" style="left:32px;top:46px;font-size:8.5px;line-height:10px">Click to edit Master text styles</div>
  <div class="bullet" style="left:46px;top:60px;font-size:7.5px;line-height:9px">Second level</div>
  <div class="bullet" style="left:61px;top:74px;font-size:6.5px;line-height:8px">Third level</div>
  <div class="bullet" style="left:77px;top:86px;font-size:5.8px;line-height:7px">Fourth level</div>
  <div class="bullet" style="left:94px;top:97px;font-size:5.5px;line-height:7px">Fifth level</div>
  <div class="foot"><span class="word">Corvane</span><span class="dot"></span></div>
</section>

<section class="slide" style="left:874.3px;top:45.2px">
  <div class="header"><div class="title">Click to edit Master title style</div></div>
  <div role="img" aria-label="Photo or chart placeholder" style="left:21px;top:40px;width:107px;height:95px;border-radius:4px;background:var(--teal)"></div>
  <div style="left:160px;top:46px;font-size:6.3px;line-height:7px;white-space:nowrap">Click to edit Master text styles</div>
  <div class="bullet" style="left:151px;top:56px;font-size:5.8px;line-height:7px">Click to edit Master text styles</div>
  <div class="bullet" style="left:162px;top:65.5px;font-size:5px;line-height:6px">Second level</div>
  <div class="bullet" style="left:173px;top:75px;font-size:4.5px;line-height:5px">Third level</div>
  <div class="bullet" style="left:183px;top:83px;font-size:3.8px;line-height:4px">Fourth level</div>
  <div class="bullet" style="left:195px;top:90.5px;font-size:3.5px;line-height:4px">Fifth level</div>
  <div class="foot"><span class="word">Corvane</span><span class="dot"></span></div>
</section>

<!-- Row 2 -->
<section class="slide on-teal" style="left:46.6px;top:204px;background:var(--teal)">
  <div class="title" style="left:31.7px;top:47px;font-size:10.5px;line-height:12.5px">Click to edit Master<br>title style</div>
  <div style="left:31.7px;top:79px;font-size:5.3px;line-height:6px;color:var(--white)">Click to edit Master text styles</div>
  <div style="left:150px;top:38px;font-size:5.3px;line-height:6px;color:var(--white);white-space:nowrap">Click to edit Master text styles</div>
  <div style="left:150px;top:53px;width:88px;font-size:4.5px;line-height:5.7px;color:var(--white)">Lorem ipsum dolor sit amet, consec-tetuer adipiscing elit, sed diam nonummy nibh euismod tincidunt ut laoreet dolore magna aliquam erat volutpat. Ut wisi enim ad minim veniam, quis nostrud exerci tation ullamcorper suscipit lobortis nisl ut aliquip ex ea commodo conse-quat.<br><br>Duis autem vel eum iriure dolor in hen-drerit in vulputate velit esse molestie consequat, vel illum dolore eu</div>
  <div class="foot"><span class="word">Corvane</span><span class="dot"></span></div>
</section>

<section class="slide" style="left:321.4px;top:204px">
  <div class="header"><div class="title">Click to edit Master title style</div></div>
  <div class="body" style="left:20px;top:38px;width:220px">Lorem ipsum dolor sit amet, consectetuer adipiscing elit, sed diam nonummy nibh euismod tincidunt ut laoreet dolore magna aliquam erat volutpat. Ut wisi enim ad minim veniam, quis nostrud exerci tation ullamcorper suscipit lobortis nisl ut aliquip</div>
  <svg style="left:8px;top:62px" width="40" height="40" viewBox="0 0 40 40"><circle cx="20" cy="19" r="18" fill="none" stroke="var(--teal)" stroke-width="1"/><use href="#i-heart" x="10" y="9" width="20" height="20" style="color:var(--purple)"/></svg>
  <div class="tiny" style="left:20px;top:103px;width:52px">Lorem ipsum dolor sit amet, consectetuer adipiscing elit, sed diam nonummy nibh euis-mod tincidunt ut laoreet dolore magna aliquam erat volutpat. Ut wisi enim ad minim veniam, quis nostrud exerci tation ullamcorper suscipit lobortis nisl ut aliquip</div>
  <svg style="left:114px;top:62px" width="38" height="66" viewBox="0 0 38 66"><rect x="1" y="1" width="36" height="64" rx="4" fill="none" stroke="var(--gray)" stroke-width="1.2"/><line x1="1" y1="9" x2="37" y2="9" stroke="var(--gray)" stroke-width="1"/><line x1="1" y1="53" x2="37" y2="53" stroke="var(--gray)" stroke-width="1"/><line x1="16" y1="5" x2="22" y2="5" stroke="var(--gray)" stroke-width="1"/><circle cx="19" cy="59" r="3" fill="none" stroke="var(--gray)" stroke-width="1.2"/></svg>
  <svg style="left:191px;top:60px" width="40" height="40" viewBox="0 0 40 40"><circle cx="20" cy="19" r="18" fill="none" stroke="var(--teal)" stroke-width="1"/><use href="#i-folder" x="10" y="9" width="20" height="20" style="color:var(--purple)"/></svg>
  <div class="tiny" style="left:186px;top:101px;width:52px">Lorem ipsum dolor sit amet, consectetuer adipiscing elit, sed diam nonummy nibh euis-mod tincidunt ut laoreet dolore magna aliquam erat volutpat. Ut wisi enim ad minim veniam, quis nostrud exerci tation ullamcorper suscipit lobortis nisl ut aliquip</div>
  <div class="foot"><span class="word">Corvane</span><span class="dot"></span></div>
</section>

<section class="slide" style="left:597.2px;top:204px">
  <div class="header"><div class="title">Click to edit Master title style</div></div>
  <svg style="left:19px;top:37.6px" width="32" height="32" viewBox="0 0 32 32"><circle cx="16" cy="16" r="14" fill="none" stroke="var(--gray-light)" stroke-width="3.5"/><circle cx="16" cy="16" r="14" fill="none" stroke="var(--teal)" stroke-width="3.5" pathLength="100" stroke-dasharray="25 100" transform="rotate(-90 16 16)"/><text x="16" y="19.5" text-anchor="middle" font-family="Oswald,sans-serif" font-size="10" fill="var(--gray)">25%</text></svg>
  <svg style="left:59px;top:37.6px" width="32" height="32" viewBox="0 0 32 32"><circle cx="16" cy="16" r="14" fill="none" stroke="var(--gray-light)" stroke-width="3.5"/><circle cx="16" cy="16" r="14" fill="none" stroke="var(--teal)" stroke-width="3.5" pathLength="100" stroke-dasharray="50 100" transform="rotate(-90 16 16)"/><text x="16" y="19.5" text-anchor="middle" font-family="Oswald,sans-serif" font-size="10" fill="var(--gray)">50%</text></svg>
  <svg style="left:99px;top:37.6px" width="32" height="32" viewBox="0 0 32 32"><circle cx="16" cy="16" r="14" fill="none" stroke="var(--gray-light)" stroke-width="3.5"/><circle cx="16" cy="16" r="14" fill="none" stroke="var(--teal)" stroke-width="3.5" pathLength="100" stroke-dasharray="75 100" transform="rotate(-90 16 16)"/><text x="16" y="19.5" text-anchor="middle" font-family="Oswald,sans-serif" font-size="10" fill="var(--gray)">75%</text></svg>
  <div style="left:151.6px;top:40px;width:97px;height:6.5px;background:var(--teal)"><span style="right:3px;top:1.5px;font-size:3px;line-height:3.5px;color:var(--white)">$1,000,000</span></div>
  <div style="left:151.6px;top:50.3px;width:62px;height:6.5px;background:var(--teal)"><span style="right:3px;top:1.5px;font-size:3px;line-height:3.5px;color:var(--white)">$1,200,000</span></div>
  <div style="left:151.6px;top:60px;width:58px;height:6.5px;background:var(--teal)"><span style="right:3px;top:1.5px;font-size:3px;line-height:3.5px;color:var(--white)">$1,500,000</span></div>
  <div class="tiny c" style="left:35px;top:83.5px">AB</div><div class="tiny c" style="left:52px;top:83.5px">CD</div><div class="tiny c" style="left:77px;top:83.5px">EF</div><div class="tiny c" style="left:103px;top:83.5px">GH</div><div class="tiny c" style="left:127px;top:83.5px">IJ</div><div class="tiny c" style="left:154px;top:83.5px">KL</div><div class="tiny c" style="left:180px;top:83.5px">MN</div><div class="tiny c" style="left:205px;top:83.5px">OP</div><div class="tiny c" style="left:230px;top:83.5px">QR</div>
  <div style="left:24.7px;top:89.4px;width:223px;height:13px;border:.5px solid var(--gray-light)"></div>
  <div style="left:45px;top:90px;width:.5px;height:12px;background:var(--gray-light)"></div>
  <div class="c" style="left:35px;top:92.5px;font-family:Catamaran,sans-serif;font-size:6.5px;line-height:7px;color:var(--teal)">Total</div>
  <div class="tiny-dark c" style="left:52px;top:94.5px">2016</div><div class="tiny-dark c" style="left:77px;top:94.5px;white-space:nowrap">+ 20,000,000</div>
  <div class="tiny-dark c" style="left:103px;top:94.5px">2016</div><div class="tiny-dark c" style="left:128px;top:94.5px;white-space:nowrap">+ 20,000,000</div>
  <div class="tiny-dark c" style="left:154px;top:94.5px">2016</div><div class="tiny-dark c" style="left:179px;top:94.5px;white-space:nowrap">+ 20,000,000</div>
  <div class="tiny-dark c" style="left:205px;top:94.5px">2016</div><div class="tiny-dark c" style="left:230px;top:94.5px;white-space:nowrap">+ 20,000,000</div>
  <div class="body" style="left:20.5px;top:112px;width:220px">Lorem ipsum dolor sit amet, consectetuer adipiscing elit, sed diam nonummy nibh euismod tincidunt ut laoreet dolore magna aliquam erat volutpat. Ut wisi enim ad minim veniam, quis nostrud exerci tation ullamcorper suscipit lobortis nisl ut aliquip</div>
  <div class="foot"><span class="word">Corvane</span><span class="dot"></span></div>
</section>

<section class="slide" style="left:874.3px;top:204px">
  <div class="header"><div class="title">Click to edit Master title style</div></div>
  <div class="body" style="left:21px;top:38px;width:220px">Lorem ipsum dolor sit amet, consectetuer adipiscing elit, sed diam nonummy nibh euismod tincidunt ut laoreet dolore magna aliquam erat volutpat. Ut wisi enim ad minim veniam, quis nostrud exerci tation ullamcorper suscipit lobortis nisl ut aliquip</div>
  <div class="c" style="left:59px;top:67px;font-size:8px;line-height:9px">2013</div>
  <div class="c" style="left:109px;top:67px;font-size:8px;line-height:9px">2014</div>
  <div class="c" style="left:159px;top:67px;font-size:8px;line-height:9px">2015</div>
  <div class="c" style="left:209px;top:67px;font-size:8px;line-height:9px">2016</div>
  <div class="c" style="left:59px;top:77.6px;width:45px;height:10.7px;background:var(--teal);color:var(--white);font-size:4.5px;line-height:10.7px">PROFIT 40%</div>
  <div class="c" style="left:109px;top:77.6px;width:45px;height:10.7px;background:var(--teal);color:var(--white);font-size:4.5px;line-height:10.7px">PROFIT 30%</div>
  <div class="c" style="left:159px;top:77.6px;width:45px;height:10.7px;background:var(--teal);color:var(--white);font-size:4.5px;line-height:10.7px">PROFIT 45%</div>
  <div class="c" style="left:209px;top:77.6px;width:45px;height:10.7px;background:var(--teal);color:var(--white);font-size:4.5px;line-height:10.7px">PROFIT 60%</div>
  <svg style="left:53px;top:96px;color:var(--gray)" width="12" height="12"><use href="#i-gear" width="12" height="12"/></svg>
  <svg style="left:103px;top:96px;color:var(--gray)" width="12" height="12"><use href="#i-bulb" width="12" height="12"/></svg>
  <svg style="left:153px;top:96px;color:var(--gray)" width="12" height="12"><use href="#i-folder" width="12" height="12"/></svg>
  <svg style="left:203px;top:96px;color:var(--gray)" width="12" height="12"><use href="#i-heart" width="12" height="12"/></svg>
  <div class="tiny c" style="left:59px;top:112px;white-space:nowrap">Lorem Ipsum</div>
  <div class="tiny c" style="left:109px;top:112px;white-space:nowrap">Lorem Ipsum</div>
  <div class="tiny c" style="left:159px;top:112px;white-space:nowrap">Lorem Ipsum</div>
  <div class="tiny c" style="left:209px;top:112px;white-space:nowrap">Lorem Ipsum</div>
  <div class="foot"><span class="word">Corvane</span><span class="dot"></span></div>
</section>

<!-- Row 3 -->
<section class="slide" style="left:46.6px;top:364.7px">
  <div class="header"><div class="title">Click to edit Master title style</div></div>
  <div style="left:82.4px;top:52.6px;width:48.5px;height:63.4px;background:var(--teal)"></div>
  <div style="left:188.8px;top:52.6px;width:48.5px;height:63.4px;background:var(--teal)"></div>
  <svg style="left:46px;top:64.5px;color:var(--gray)" width="14" height="14"><use href="#i-gear" width="14" height="14"/></svg>
  <svg style="left:100px;top:64.5px;color:var(--white)" width="14" height="14"><use href="#i-bulb" width="14" height="14"/></svg>
  <svg style="left:153px;top:64.5px;color:var(--gray)" width="14" height="14"><use href="#i-folder" width="14" height="14"/></svg>
  <svg style="left:207px;top:64.5px;color:var(--white)" width="14" height="14"><use href="#i-heart" width="14" height="14"/></svg>
  <div class="label c" style="left:53px;top:85.5px">Lorem Ipsum</div>
  <div class="label c" style="left:107px;top:85.5px;color:var(--white)">Lorem Ipsum</div>
  <div class="label c" style="left:160px;top:85.5px">Lorem Ipsum</div>
  <div class="label c" style="left:214px;top:85.5px;color:var(--white)">Lorem Ipsum</div>
  <div class="tiny-dark c" style="left:53px;top:93px;width:44px">Lorem ipsum dolor sit amet, consectetur adipiscing elit. Vivamus porta leo quis pellentesque viverra. Nam et urna gravida, pretium erat in, consectetur est.</div>
  <div class="tiny-dark c" style="left:107px;top:93px;width:44px;color:var(--white)">Lorem ipsum dolor sit amet, consectetur adipiscing elit. Vivamus porta leo quis pellentesque viverra. Nam et urna gravida, pretium erat in, consectetur est.</div>
  <div class="tiny-dark c" style="left:160px;top:93px;width:44px">Lorem ipsum dolor sit amet, consectetur adipiscing elit. Vivamus porta leo quis pellentesque viverra. Nam et urna gravida, pretium erat in, consectetur est.</div>
  <div class="tiny-dark c" style="left:214px;top:93px;width:44px;color:var(--white)">Lorem ipsum dolor sit amet, consectetur adipiscing elit. Vivamus porta leo quis pellentesque viverra. Nam et urna gravida, pretium erat in, consectetur est.</div>
  <div class="foot"><span class="word">Corvane</span><span class="dot"></span></div>
</section>

<section class="slide" style="left:321.4px;top:364.7px">
  <div class="header"><div class="title">Click to edit Master title style</div></div>
  <svg style="left:21.5px;top:42.5px" width="17" height="17" viewBox="0 0 17 17"><circle cx="8.5" cy="8.5" r="7.8" fill="none" stroke="var(--teal)" stroke-width="1"/><use href="#i-gear" x="3.5" y="3.5" width="10" height="10" style="color:var(--gray)"/></svg>
  <div class="tiny" style="left:42.6px;top:47px;width:190px;font-size:3.1px;line-height:4px;color:var(--ink)">Lorem ipsum dolor sit amet, consectetuer adipiscing elit, sed diam nonummy nibh euismod tincidunt ut laoreet dolore magna ali-quam erat volutpat. Ut wisi enim ad minim veniam, quis nostrud exerci tation ullamcorper suscipit lobortis nisl ut aliquip</div>
  <svg style="left:21.5px;top:66px" width="17" height="17" viewBox="0 0 17 17"><circle cx="8.5" cy="8.5" r="7.8" fill="none" stroke="var(--teal)" stroke-width="1"/><use href="#i-bulb" x="3.5" y="3.5" width="10" height="10" style="color:var(--gray)"/></svg>
  <div class="tiny" style="left:42.6px;top:71px;width:190px;font-size:3.1px;line-height:4px;color:var(--ink)">Lorem ipsum dolor sit amet, consectetuer adipiscing elit, sed diam nonummy nibh euismod tincidunt ut laoreet dolore magna ali-quam erat volutpat. Ut wisi enim ad minim veniam, quis nostrud exerci tation ullamcorper suscipit lobortis nisl ut aliquip</div>
  <svg style="left:21.5px;top:90px" width="17" height="17" viewBox="0 0 17 17"><circle cx="8.5" cy="8.5" r="7.8" fill="none" stroke="var(--teal)" stroke-width="1"/><use href="#i-folder" x="3.5" y="3.5" width="10" height="10" style="color:var(--gray)"/></svg>
  <div class="tiny" style="left:42.6px;top:95px;width:190px;font-size:3.1px;line-height:4px;color:var(--ink)">Lorem ipsum dolor sit amet, consectetuer adipiscing elit, sed diam nonummy nibh euismod tincidunt ut laoreet dolore magna ali-quam erat volutpat. Ut wisi enim ad minim veniam, quis nostrud exerci tation ullamcorper suscipit lobortis nisl ut aliquip</div>
  <svg style="left:21.5px;top:114px" width="17" height="17" viewBox="0 0 17 17"><circle cx="8.5" cy="8.5" r="7.8" fill="none" stroke="var(--teal)" stroke-width="1"/><use href="#i-heart" x="3.5" y="3.5" width="10" height="10" style="color:var(--gray)"/></svg>
  <div class="tiny" style="left:42.6px;top:119px;width:190px;font-size:3.1px;line-height:4px;color:var(--ink)">Lorem ipsum dolor sit amet, consectetuer adipiscing elit, sed diam nonummy nibh euismod tincidunt ut laoreet dolore magna ali-quam erat volutpat. Ut wisi enim ad minim veniam, quis nostrud exerci tation ullamcorper suscipit lobortis nisl ut aliquip</div>
  <div class="foot"><span class="word">Corvane</span><span class="dot"></span></div>
</section>

<section class="slide" style="left:597.2px;top:364.7px">
  <div class="header"><div class="title">Click to edit Master title style</div></div>
  <svg style="left:18.5px;top:44.5px" width="45" height="45" viewBox="0 0 45 45"><circle cx="22.5" cy="22.5" r="20" fill="none" stroke="var(--gray)" stroke-width="3.8"/><circle cx="22.5" cy="22.5" r="20" fill="none" stroke="var(--teal)" stroke-width="3.8" pathLength="100" stroke-dasharray="25 100" transform="rotate(-90 22.5 22.5)"/><text x="22.5" y="27.5" text-anchor="middle" font-family="Oswald,sans-serif" font-size="13.5" fill="var(--teal)">25%</text></svg>
  <svg style="left:80px;top:44.5px" width="45" height="45" viewBox="0 0 45 45"><circle cx="22.5" cy="22.5" r="20" fill="none" stroke="var(--gray)" stroke-width="3.8"/><circle cx="22.5" cy="22.5" r="20" fill="none" stroke="var(--teal)" stroke-width="3.8" pathLength="100" stroke-dasharray="50 100" transform="rotate(-90 22.5 22.5)"/><text x="22.5" y="27.5" text-anchor="middle" font-family="Oswald,sans-serif" font-size="13.5" fill="var(--teal)">50%</text></svg>
  <svg style="left:141px;top:44.5px" width="45" height="45" viewBox="0 0 45 45"><circle cx="22.5" cy="22.5" r="20" fill="none" stroke="var(--gray)" stroke-width="3.8"/><circle cx="22.5" cy="22.5" r="20" fill="none" stroke="var(--teal)" stroke-width="3.8" pathLength="100" stroke-dasharray="75 100" transform="rotate(-90 22.5 22.5)"/><text x="22.5" y="27.5" text-anchor="middle" font-family="Oswald,sans-serif" font-size="13.5" fill="var(--teal)">75%</text></svg>
  <svg style="left:202.5px;top:44.5px" width="45" height="45" viewBox="0 0 45 45"><circle cx="22.5" cy="22.5" r="20" fill="none" stroke="var(--teal)" stroke-width="3.8"/><text x="22.5" y="27.5" text-anchor="middle" font-family="Oswald,sans-serif" font-size="13.5" fill="var(--teal)">100%</text></svg>
  <div class="label c" style="left:41px;top:103px;font-size:6px">Lorem Ipsum</div>
  <div class="label c" style="left:102.5px;top:103px;font-size:6px">Lorem Ipsum</div>
  <div class="label c" style="left:163.5px;top:103px;font-size:6px">Lorem Ipsum</div>
  <div class="label c" style="left:225px;top:103px;font-size:6px">Lorem Ipsum</div>
  <div class="tiny-dark c" style="left:41px;top:110px;width:50px;color:var(--ink)">Lorem ipsum dolor sit amet, consectetur adipiscing elit. Vivamus porta leo quis pellentesque viverra. Nam et urna gravida, pretium erat in, consectetur est.</div>
  <div class="tiny-dark c" style="left:102.5px;top:110px;width:50px;color:var(--ink)">Lorem ipsum dolor sit amet, consectetur adipiscing elit. Vivamus porta leo quis pellentesque viverra. Nam et urna gravida, pretium erat in, consectetur est.</div>
  <div class="tiny-dark c" style="left:163.5px;top:110px;width:50px;color:var(--ink)">Lorem ipsum dolor sit amet, consectetur adipiscing elit. Vivamus porta leo quis pellentesque viverra. Nam et urna gravida, pretium erat in, consectetur est.</div>
  <div class="tiny-dark c" style="left:225px;top:110px;width:50px;color:var(--ink)">Lorem ipsum dolor sit amet, consectetur adipiscing elit. Vivamus porta leo quis pellentesque viverra. Nam et urna gravida, pretium erat in, consectetur est.</div>
  <div class="foot"><span class="word">Corvane</span><span class="dot"></span></div>
</section>

<section class="slide" style="left:874.3px;top:364.7px">
  <div style="left:0;top:0;width:267px;height:106.7px;background:var(--teal)"></div>
  <div class="title c" style="left:133.5px;top:60px;font-size:10.5px;line-height:13px">Thank You!</div>
  <div class="signoff"><span class="word">Corvane</span><span class="dot"></span></div>
</section>

</body>
</html>
```